Northern Plains Trades Motor Guild
Where Small Business Matters
Simple
Marco Brenn
President & CEO
214 - 27480 Corbett Rd
Box 46712 Ferncliff
Alder Bend, BC
V2K 4N7
marcobrenn@nptmg.example
www.nptmg.example

```html
<!DOCTYPE html>
<html lang="en">
<head>
<meta charset="utf-8">
<title>Northern Plains Trades Motor Guild — Stationery</title>
<link rel="stylesheet" href="https://fonts.googleapis.com/css2?family=Arimo:wght@400;700&display=swap">
<style>
:root{
  --paper:#ffffff;
  --bg:#ffffff;
  --rule:#d9dde3;
  --blue:#1c4a9b;
  --blue-light:#5d8fd6;
  --ink:#3a3f47;
  --ghost:#e8edf4;
  --shadow:rgba(0,0,0,.18);
}
*{box-sizing:border-box;margin:0;padding:0}
html,body{width:1200px;height:482px;overflow:hidden;background:var(--bg);font-family:'Arimo',Arial,sans-serif;color:var(--ink)}
.stage{position:relative;width:1200px;height:482px}
.frame-rule{position:absolute;left:0;width:1200px;height:1px;background:var(--rule)}
.frame-rule.top{top:12px}.frame-rule.bottom{top:468px}
.sheet{position:absolute;background:var(--paper);box-shadow:0 1px 4px var(--shadow);overflow:hidden}
.band{position:absolute;left:0;right:0;top:0;height:8px;background:linear-gradient(90deg,var(--blue) 0%,var(--blue-light) 60%,#c9d8ef 100%)}
.brand{position:absolute;display:flex;align-items:center;gap:4px;color:var(--blue);font-weight:700;letter-spacing:.5px;white-space:nowrap}
.brand .dot{border-radius:50%;background:var(--blue);flex:none}
.ghost-brand{position:absolute;color:var(--ghost);font-weight:700;letter-spacing:2px;text-align:center;white-space:nowrap}
.address{position:absolute;font-size:5.5px;line-height:7px;color:var(--ink);white-space:nowrap}
.fax-form{position:absolute;left:20px;top:112px;width:258px;font-size:6px}
.fax-row{display:flex;gap:14px;margin-bottom:9px}
.fax-field{flex:1;display:flex;align-items:flex-end;gap:4px}
.fax-field span{width:26px}
.fax-field i{flex:1;border-bottom:.8px solid #9aa3ae;height:7px}
.checks{display:flex;justify-content:space-between;margin-top:4px;font-size:5.5px}
.checks label{display:flex;align-items:center;gap:2px}
.checks b{width:6px;height:6px;border:.8px solid #7a828c;display:inline-block}
.envelope-back svg{position:absolute;left:0;top:0}
.card .address{font-size:3.2px;line-height:4.2px}
</style>
</head>
<body>
<div class="stage">
  <div class="frame-rule top"></div>
  <div class="frame-rule bottom"></div>

  <section class="sheet fax-sheet" style="left:41px;top:36px;width:296px;height:408px">
    <div class="band"></div>
    <div class="brand" style="left:14px;top:16px;font-size:15px"><span class="dot" style="width:10px;height:10px"></span>NPTMG</div>
    <div class="address" style="left:14px;top:44px">214 - 27480 Corbett Rd<br>Box 46712 Ferncliff<br>Alder Bend, BC V2K 4N7<br>Tel 604.555.0142<br>Fax 604.555.0187<br>marcobrenn@nptmg.example</div>
    <div class="fax-form">
      <div class="fax-row"><div class="fax-field"><span>To:</span><i></i></div><div class="fax-field"><span>From:</span><i></i></div></div>
      <div class="fax-row"><div class="fax-field"><span>Fax:</span><i></i></div><div class="fax-field"><span>Pages:</span><i></i></div></div>
      <div class="fax-row"><div class="fax-field"><span>Phone:</span><i></i></div><div class="fax-field"><span>Date:</span><i></i></div></div>
      <div class="fax-row"><div class="fax-field"><span>Re:</span><i></i></div><div class="fax-field"><span>CC:</span><i></i></div></div>
      <div class="checks">
        <label><b></b>Urgent</label><label><b></b>For Review</label><label><b></b>Please Comment</label><label><b></b>Please Reply</label><label><b></b>Please Recycle</label>
      </div>
    </div>
    <div class="ghost-brand" style="left:0;right:0;top:310px;font-size:56px">NPTMG</div>
  </section>

  <section class="sheet envelope-front" style="left:392px;top:92px;width:344px;height:156px">
    <div class="band"></div>
    <div class="brand" style="left:12px;top:15px;font-size:14px"><span class="dot" style="width:9px;height:9px"></span>NPTMG</div>
    <div class="address" style="left:12px;top:40px">214 - 27480 Corbett Rd<br>Box 46712 Ferncliff<br>Alder Bend, BC V2K 4N7</div>
    <div class="ghost-brand" style="left:140px;right:10px;top:70px;font-size:46px">NPTMG</div>
  </section>

  <section class="sheet envelope-back" style="left:392px;top:258px;width:344px;height:156px">
    <svg width="344" height="156" viewBox="0 0 344 156" aria-hidden="true">
      <polyline points="0,0 172,62 344,0" fill="none" stroke="#b9c0ca" stroke-width="1"/>
      <line x1="0" y1="156" x2="142" y2="70" stroke="#e2e6eb" stroke-width="1"/>
      <line x1="344" y1="156" x2="202" y2="70" stroke="#e2e6eb" stroke-width="1"/>
    </svg>
    <div class="brand" style="left:0;right:0;top:28px;justify-content:center;font-size:14px"><span class="dot" style="width:9px;height:9px"></span>NPTMG</div>
  </section>

  <section class="sheet letterhead" style="left:794px;top:36px;width:300px;height:408px">
    <div class="band"></div>
    <div class="brand" style="left:14px;top:16px;font-size:15px"><span class="dot" style="width:10px;height:10px"></span>NPTMG</div>
    <div class="address" style="left:14px;top:44px">214 - 27480 Corbett Rd<br>Box 46712 Ferncliff<br>Alder Bend, BC V2K 4N7<br>Tel 604.555.0142<br>Fax 604.555.0187<br>www.nptmg.example</div>
    <div class="ghost-brand" style="left:0;right:0;top:300px;font-size:56px">NPTMG</div>
  </section>

  <section class="sheet card card-front" style="left:1037px;top:88px;width:68px;height:42px">
    <div class="band" style="height:3px"></div>
    <div class="brand" style="left:4px;top:6px;font-size:7px;gap:2px"><span class="dot" style="width:4px;height:4px"></span>NPTMG</div>
    <div class="address" style="left:4px;top:20px">Marco Brenn, President &amp; CEO<br>214 - 27480 Corbett Rd, Alder Bend<br>marcobrenn@nptmg.example</div>
  </section>

  <section class="sheet card card-back" style="left:1037px;top:160px;width:68px;height:48px">
    <div class="brand" style="left:0;right:0;top:17px;justify-content:center;font-size:9px;gap:3px"><span class="dot" style="width:5px;height:5px"></span>NPTMG</div>
    <div class="band" style="top:auto;bottom:0;height:3px"></div>
  </section>
</div>
</body>
</html>
```